Time for a better IT consulting company?

We are a mobile computer consulting company, taking care of client's issues remotely or at their site. Website of company www.qr-lumotek.com. Business card is an example of marketing so far.
We moved this year but we still service our existing clients. We have expanded our number of technicians available. We would like to use this card for both new business and reaching out to old business.

Target Market(s)

This should target businesses and referrals to businesses from our existing clients as well as a new client outreach for our new location.

Industry/Entity Type

Computer

Requirements
Must have
• This postcard will let clients know we have moved into or we continue to service their area. Make sure it says Inc, not LLC. Must incorporate existing theme in some fashion.
Nice to have
• Themes to communicate: team of people standing by, stability, faster response time, accessibility.
• Areas of coverage: Westchester, Rockland, Manhattan, The Bronx, lower Connecticut.
Should not have
• Cartoon feel.

```html
<!DOCTYPE html>
<html lang="en">
<head>
<meta charset="utf-8">
<title>Lumotek Computer Consulting Postcard</title>
<link href="https://fonts.googleapis.com/css2?family=Archivo+Black&family=Lato:wght@400;700&display=swap" rel="stylesheet">
<style>
  :root {
    --bg: #2a2a2a;
    --navy: #0f3f5e;
    --blue: #17628c;
    --cyan: #2fa8dc;
    --sky: #5cc8f2;
    --white: #ffffff;
    --ink: #1d2a33;
    --paper-grey: #e9ecee;
    --rule: #555c61;
  }
  * { margin: 0; padding: 0; box-sizing: border-box; }
  html, body { width: 902px; height: 1200px; overflow: hidden; background: var(--bg); }
  .canvas { position: relative; width: 902px; height: 1200px; }

  .card { position: absolute; left: 107px; width: 703px; overflow: hidden; background: var(--white); }
  .card svg.shapes { position: absolute; inset: 0; }
  .front { top: 30px; height: 548px; }
  .back { top: 615px; height: 545px; }

  .heading-font { font-family: "Archivo Black", "Arial Black", sans-serif; }

  .front .url {
    position: absolute; right: 24px; top: 20px;
    font-family: "Archivo Black", sans-serif; font-size: 18px; color: var(--white); letter-spacing: .5px;
  }
  .brand { position: absolute; display: flex; flex-direction: column; align-items: center; }
  .brand .dot { width: 58px; height: 58px; border-radius: 50%; background: var(--blue); margin-bottom: 8px; }
  .brand .name { font-family: "Archivo Black", sans-serif; font-size: 20px; color: var(--navy); letter-spacing: 1px; }
  .front .brand { left: 470px; top: 250px; }

  .headline { position: absolute; left: 38px; top: 458px; color: var(--white); font-family: "Archivo Black", sans-serif; line-height: 1.25; }
  .headline .big { font-size: 25px; letter-spacing: .5px; }
  .headline .small { font-size: 21px; }

  .social { position: absolute; left: 577px; top: 494px; display: flex; gap: 16px; }
  .social span { width: 22px; height: 22px; background: var(--white); opacity: .85; border-radius: 3px; }

  .back .content { position: absolute; left: 24px; top: 22px; width: 330px; color: var(--white); font-family: "Lato", sans-serif; }
  .welcome { font-family: "Archivo Black", sans-serif; font-size: 15.5px; color: var(--sky); line-height: 1.2; }
  .intro { font-size: 12.4px; line-height: 1.28; margin-top: 4px; }
  .pill {
    display: inline-block; background: linear-gradient(#fff, #d8dcdf); color: var(--ink);
    font-family: "Archivo Black", sans-serif; font-size: 16px; padding: 1px 12px 1px 26px;
    border-radius: 0 14px 14px 0; margin-left: -24px;
  }
  .services-title { margin-top: 12px; }
  .services { list-style: none; display: grid; grid-template-columns: 156px 180px; row-gap: 9px; margin-top: 10px; font-size: 13px; font-weight: 700; }
  .services li { position: relative; padding-left: 17px; }
  .services li::before { content: ""; position: absolute; left: 2px; top: 5px; width: 7px; height: 7px; border-radius: 50%; background: var(--white); }
  .services .wide { grid-column: 1 / 3; }
  .compliment { font-size: 13px; font-weight: 700; margin-top: 12px; line-height: 1.25; }
  .thanks { font-family: "Archivo Black", sans-serif; font-size: 15.5px; margin-top: 9px; }
  .contact-title { margin-top: 10px; }
  .contacts { list-style: none; margin-top: 10px; font-size: 12.5px; font-weight: 700; }
  .contacts li { display: flex; align-items: center; gap: 7px; margin-bottom: 7px; }
  .contacts svg { width: 10px; height: 10px; }

  .back .brand { left: 372px; top: 30px; }
  .back .brand .dot { width: 44px; height: 44px; }
  .back .brand .name { font-size: 16px; }

  .stamp { position: absolute; left: 599px; top: 30px; width: 76px; height: 96px; border: 1.5px solid var(--ink); }
  .address-line { position: absolute; left: 478px; width: 197px; height: 1.5px; background: var(--rule); }
  .back .url {
    position: absolute; right: 30px; bottom: 14px;
    font-family: "Archivo Black", sans-serif; font-size: 17px; color: var(--white); letter-spacing: .5px;
  }
</style>
</head>
<body>
<div class="canvas">

  <section class="card front">
    <svg class="shapes" width="703" height="548" viewBox="0 0 703 548">
      <defs>
        <linearGradient id="keyboardTone" x1="0" y1="0" x2="1" y2="1">
          <stop offset="0" stop-color="#f4f5f6"/>
          <stop offset=".6" stop-color="#dfe2e4"/>
          <stop offset="1" stop-color="#c9cdd0"/>
        </linearGradient>
        <linearGradient id="bandTone" x1="0" y1="0" x2="1" y2="1">
          <stop offset="0" stop-color="#1a6a96"/>
          <stop offset="1" stop-color="#0f3f5e"/>
        </linearGradient>
      </defs>
      <rect width="703" height="548" fill="url(#keyboardTone)" role="img" aria-label="Close-up photo of a white keyboard with a blue Help key"/>
      <path d="M470 0 C505 40 560 55 640 52 C690 50 703 70 703 95 L703 0 Z" fill="url(#bandTone)"/>
      <path d="M520 52 C620 70 690 60 703 95" stroke="var(--sky)" stroke-width="4" fill="none"/>
      <path d="M0 430 C180 392 420 470 590 420 C670 395 703 330 703 230 L703 548 L0 548 Z" fill="url(#bandTone)"/>
      <path d="M0 420 C180 382 420 458 590 410 C670 385 700 320 703 220" stroke="var(--sky)" stroke-width="5" fill="none"/>
      <path d="M120 430 C300 420 460 452 600 405" stroke="var(--cyan)" stroke-width="2" fill="none" opacity=".7"/>
    </svg>
    <div class="url">www.qr-lumotek.com</div>
    <div class="brand"><span class="dot"></span><span class="name">LUMOTEK</span></div>
    <div class="headline">
      <div class="big">NEED IMMEDIATE</div>
      <div class="small">assistance with a computer issue?</div>
    </div>
    <div class="social"><span></span><span></span><span></span></div>
  </section>

  <section class="card back">
    <svg class="shapes" width="703" height="545" viewBox="0 0 703 545">
      <defs>
        <radialGradient id="panelTone" cx=".35" cy=".4" r=".8">
          <stop offset="0" stop-color="#1f6f99"/>
          <stop offset="1" stop-color="#0c3652"/>
        </radialGradient>
      </defs>
      <path d="M0 497 L703 497 L703 545 L0 545 Z" fill="var(--blue)"/>
      <path d="M0 0 L210 0 C340 20 400 140 400 285 C400 420 350 490 300 545 L0 545 Z" fill="#8d9297"/>
      <path d="M0 0 L200 0 C325 20 388 140 388 285 C388 420 338 490 288 545 L0 545 Z" fill="url(#panelTone)"/>
    </svg>
    <div class="content">
      <div class="welcome">Welcome To Lumotek<br>Computer Consulting</div>
      <p class="intro">For 18 years, my company provided computer support to residents and businesses in the Los Angeles area. At last count, we had received 85 five star ratings from our on-line clients. We have permanently relocated to Westchester County and my family and I are in love with it's charm and beauty.</p>
      <div class="pill services-title">Services Offered</div>
      <ul class="services">
        <li>IT Staffing</li><li>PC &amp; MAC</li>
        <li>Home &amp; Office</li><li>Websites and wiring</li>
        <li class="wide">Wireless and Cellular Solutions</li>
        <li class="wide">New Equipment Purchases &amp; Upgrades</li>
        <li class="wide">Hardware, Software &amp; Security Consulting</li>
        <li class="wide">Server &amp; System Monitoring &amp; Maintenance</li>
      </ul>
      <p class="compliment">The highest compliment our clients can offer are referrals.</p>
      <p class="thanks">Thanks you for your business!!</p>
      <div class="pill contact-title">Contact Us</div>
      <ul class="contacts">
        <li><svg viewBox="0 0 10 10"><rect x="2" y="0" width="6" height="10" rx="1" fill="#fff"/></svg>555.014.2290</li>
        <li><svg viewBox="0 0 10 10"><rect x="0" y="2" width="10" height="7" fill="#fff"/><path d="M0 2 L5 6 L10 2" stroke="#0f3f5e" fill="none"/></svg>info@qr-lumotek.com</li>
        <li><svg viewBox="0 0 10 10"><path d="M5 0 L10 5 L8.5 5 L8.5 10 L1.5 10 L1.5 5 L0 5 Z" fill="#fff"/></svg>Lumotek Computer Consulting</li>
      </ul>
    </div>
    <div class="brand"><span class="dot"></span><span class="name">LUMOTEK</span></div>
    <div class="stamp"></div>
    <div class="address-line" style="top:281px"></div>
    <div class="address-line" style="top:327px"></div>
    <div class="address-line" style="top:373px"></div>
    <div class="url">www.qr-lumotek.com</div>
  </section>

</div>
</body>
</html>
```